Lumvex Crating Business Card

Project Overview
We are seeking a modern, minimalist business card that effectively represents our company while making a bold and lasting impression. The design should reflect trust, professionalism, and innovation, reinforcing our expertise in custom plastic manufacturing for warehouse and distribution centers.

Provided Assets & Specifications
Logo: We will provide our official logo for integration into the design.
Design Files: Photoshop (PSD) files for our printing specifications will be supplied.

Card Size & Material:
Dimensions: 3.5" x 2"
Material: 1/8" Radius Plastic Business Cards with 1/8" Rounded Corners
Clear plastic background—the design should strategically incorporate transparency.
Orientation: The card should be designed in landscape format for a sleek and professional presentation.

Design Requirements:
Logo Prominence
The logo must be the focal point of the card.
Space should be used effectively to draw attention to the logo while maintaining a minimalist layout.

Clear Plastic Integration
The transparent background should create the illusion of blank space, enhancing the modern and high-quality feel.
Avoid any frosted effects—we do not want white areas to appear semi-transparent.

Minimalist & Impactful
Clean, structured, and easy to read at a glance.
Focus on sharp contrast to ensure legibility and visibility.
The design should instill confidence and reflect our role as a leading plastics manufacturer.

Color Palette & Contrast
Primary Colors: Blue, Black, White, and Grey
Use bold black or blue for text and key elements to ensure they stand out against the clear plastic.
Avoid light, pastel, or neon colors that may fade into the plastic background.
No frosted or semi-transparent white—we do not want a cloudy effect.

Typography & Information Hierarchy
Bold, modern typography—clear, professional, and highly legible.
The business card should highlight:
Company Logo (Primary Focus)
Full Name & Title
Phone Number
Email
Website

Brand Representation
The card should reflect our expertise in manufacturing high-quality custom plastics for large-scale packaging and distribution businesses.
Our clients rely on us to enhance their brand presence through custom plastic solutions, and our business cards should reinforce that sense of precision and trust.

Final Considerations
Utilize the clear plastic effectively to differentiate our brand from standard business cards.
Maintain a sleek, professional aesthetic while ensuring all text and elements remain legible.
The design should align with our industry, conveying reliability and innovation.
We look forward to seeing a design that captures our brand identity, maximizes the clear plastic medium, and makes a strong, professional impact on our clients.

```html
<!DOCTYPE html>
<html lang="en">
<head>
<meta charset="utf-8">
<title>Lumvex Crating – Business Card</title>
<link rel="stylesheet" href="https://fonts.googleapis.com/css2?family=Roboto:wght@400;500;700&display=swap">
<style>
  :root {
    --backdrop: #e4d6c2;
    --card-fill: #f1ebe2;
    --card-edge: rgba(255, 255, 255, 0.85);
    --ink: #111111;
    --ink-soft: #2b2b2b;
    --logo-dark: #333333;
    --brand-blue: #1b8ac9;
    --shadow: rgba(80, 55, 25, 0.22);
  }
  * { margin: 0; padding: 0; box-sizing: border-box; }
  html, body {
    width: 1200px;
    height: 1196px;
    overflow: hidden;
    background: var(--backdrop);
    font-family: "Roboto", Arial, sans-serif;
  }
  .stage {
    width: 1200px;
    height: 1196px;
    display: flex;
    align-items: center;
    justify-content: center;
  }
  .business-card {
    position: relative;
    width: 940px;
    height: 537px;
    border-radius: 34px;
    background: var(--card-fill);
    border: 2px solid var(--card-edge);
    box-shadow: 0 14px 34px var(--shadow);
    color: var(--ink);
  }
  .holder {
    position: absolute;
    left: 56px;
    top: 58px;
  }
  .holder-name {
    font-size: 34px;
    font-weight: 700;
    letter-spacing: 0.2px;
    color: var(--ink);
  }
  .holder-title {
    margin-top: 2px;
    font-size: 22px;
    font-weight: 400;
    color: var(--brand-blue);
  }
  .contact {
    position: absolute;
    right: 56px;
    top: 40px;
    list-style: none;
    text-align: right;
    font-size: 22px;
    line-height: 31px;
    color: var(--ink-soft);
  }
  .wordmark {
    position: absolute;
    left: 50%;
    top: 262px;
    transform: translate(-50%, -50%);
    display: flex;
    align-items: center;
    gap: 30px;
    white-space: nowrap;
  }
  .wordmark-square {
    width: 118px;
    height: 118px;
    background: var(--brand-blue);
  }
  .wordmark-name {
    font-size: 78px;
    font-weight: 700;
    color: var(--logo-dark);
    letter-spacing: 1px;
  }
  .tagline {
    position: absolute;
    left: 0;
    right: 0;
    bottom: 58px;
    text-align: center;
    font-size: 22px;
    font-weight: 500;
    color: var(--ink-soft);
  }
</style>
</head>
<body>
  <main class="stage">
    <article class="business-card">
      <header class="holder">
        <h1 class="holder-name">Marek Ellison</h1>
        <p class="holder-title">Sales Manager</p>
      </header>

      <ul class="contact">
        <li class="contact-phone">+01 55510 48273</li>
        <li class="contact-email">marek@lumvexcrating.com</li>
        <li class="contact-web">www.lumvexcrating.com</li>
      </ul>

      <div class="wordmark">
        <span class="wordmark-square" aria-hidden="true"></span>
        <span class="wordmark-name">Lumvex Crating</span>
      </div>

      <p class="tagline">High-quality custom plastics for large-scale packaging.</p>
    </article>
  </main>
</body>
</html>
```